Harbor Nightclub

Nightclub flyer., digital single sided, for KV and PX. I included samples of some previous flyers we've used. Sample Info:
HARBOR
FRIDAYS
FRI MAY 1 2020
DJ VORTAN (club floor)
DJ RUZO & DJ TAV (residents on the lounge floor)
4217 Marlow Avenue Sacramento
www.harborvenuehall.example for list/VIP inquiries

Target Market(s)

Upscale top 40 crowd but want some cool and artsy like the examples included.

Font styles to use
Sans Serif

Requirements
Must have
• Harbor Logo
Nice to have
• Would be nice if the flyer can be incorporated later with DJ photos (sometimes we will add dj photos to pixagram etc). Would like a big city type of feel.
Should not have
• Nothing too sexual.

```html
<!DOCTYPE html>
<html lang="en">
<head>
<meta charset="utf-8">
<title>Harbor Fridays</title>
<link rel="stylesheet" href="https://fonts.googleapis.com/css2?family=Montserrat:wght@700;800;900&display=swap">
<style>
:root{
  --bg-deep:#1f1219;
  --bg-mid:#2d1a25;
  --plum:#3a1f2e;
  --wine:#3f0f2c;
  --grey:#8a8a8a;
  --white:#ffffff;
  --gold:#e8e3a0;
}
*{margin:0;padding:0;box-sizing:border-box}
html,body{width:848px;height:1200px;overflow:hidden;background:var(--bg-deep)}
.flyer{position:relative;width:848px;height:1200px;overflow:hidden;background:var(--bg-mid);font-family:"Montserrat",sans-serif;color:var(--white);text-transform:uppercase}
.backdrop{position:absolute;inset:0}
.photo-area{position:absolute;left:0;top:300px;width:640px;height:740px}
.text{position:absolute;font-weight:900;line-height:1;white-space:nowrap}
.date{top:42px;left:371px;font-size:39px;letter-spacing:1px}
.title{top:96px;left:82px;font-size:90px;letter-spacing:1px}
.lounge-djs{top:214px;left:145px;font-size:52px;letter-spacing:2px}
.lounge-note{top:268px;left:196px;font-size:21px;font-weight:800;letter-spacing:1px}
.club-dj{top:818px;left:198px;font-size:58px;letter-spacing:2px}
.club-note{top:896px;left:328px;font-size:32px;font-weight:800}
.address{top:1082px;left:48px;font-size:23px;font-weight:800;letter-spacing:.5px}
.web{top:1122px;left:48px;font-size:17px;font-weight:800;letter-spacing:.5px}
.brand{position:absolute;left:716px;top:1074px;display:flex;align-items:center;gap:6px;font-weight:900;font-size:14px;color:var(--gold)}
.brand-dot{width:10px;height:10px;border-radius:50%;background:var(--gold)}
</style>
</head>
<body>
<div class="flyer">
  <svg class="backdrop" width="848" height="1200" viewBox="0 0 848 1200">
    <rect width="848" height="1200" fill="#2d1a25"/>
    <polygon points="360,0 848,0 848,190" fill="#1e1017"/>
    <polygon points="0,330 0,1010 460,1200 848,1200 848,600 400,160" fill="#3a1f2e"/>
    <polygon points="0,1010 0,1200 460,1200" fill="#24141c"/>
    <circle cx="460" cy="565" r="275" fill="#6f6f6f" opacity=".55"/>
    <circle cx="430" cy="565" r="188" fill="#3f0f2c"/>
    <circle cx="420" cy="565" r="205" fill="none" stroke="#9a9a9a" stroke-width="1" opacity=".6"/>
    <circle cx="420" cy="565" r="265" fill="none" stroke="#aaa" stroke-width="1.5" stroke-dasharray="2 4" opacity=".5"/>
    <line x1="0" y1="365" x2="848" y2="850" stroke="#aaa" stroke-dasharray="2 4" opacity=".4"/>
    <line x1="730" y1="0" x2="300" y2="1200" stroke="#aaa" stroke-dasharray="2 4" opacity=".3"/>
    <rect x="43" y="95" width="4" height="295" fill="#777"/>
    <rect x="84" y="70" width="38" height="4" fill="#777"/>
    <rect x="782" y="1004" width="52" height="4" fill="#777"/>
    <g fill="none" stroke="#888" stroke-width="2.5">
      <rect x="40" y="3" width="10" height="10"/><rect x="40" y="31" width="10" height="10"/><rect x="40" y="59" width="10" height="10"/>
      <rect x="784" y="788" width="11" height="11"/><rect x="784" y="816" width="11" height="11"/><rect x="784" y="845" width="11" height="11"/>
      <rect x="784" y="874" width="11" height="11"/><rect x="784" y="903" width="11" height="11"/><rect x="784" y="932" width="11" height="11"/>
      <rect x="784" y="961" width="11" height="11"/>
      <circle cx="700" cy="368" r="9"/>
    </g>
    <g fill="#777"><rect x="728" y="60" width="12" height="12"/><rect x="750" y="60" width="12" height="12"/><rect x="750" y="82" width="12" height="12"/></g>
    <circle cx="621" cy="797" r="8" fill="#999"/>
  </svg>
  <div class="photo-area" role="img" aria-label="Black and white photo of a waffle cone overflowing with popcorn" style="background:radial-gradient(ellipse at 45% 40%,rgba(170,170,170,.55),rgba(110,110,110,.35) 50%,rgba(60,40,50,0) 75%)"></div>
  <div class="text date">Fri May 1 2020</div>
  <div class="text title">Fridays</div>
  <div class="text lounge-djs">DJ Ruzo &amp; DJ Tav</div>
  <div class="text lounge-note">Residents on the lounge floor</div>
  <div class="text club-dj">DJ Vortan</div>
  <div class="text club-note">Club Floor</div>
  <div class="text address">4217 Marlow Avenue Sacramento</div>
  <div class="text web">www.harborvenuehall.example for list/VIP inquiries</div>
  <div class="brand"><span class="brand-dot"></span>HARBOR</div>
</div>
</body>
</html>
```